Morvina - A new California agave spirit brand needs a label!

Hello designers! We had a lot of fun with our last project getting our logo design, now we need to put that logo onto a label!

Morvina is a company that makes agave spirit (aka Tequila but we can't call it that because of regional laws) from California grown agaves. Our goal is to make a premium quality that goes head to head with some of the best tequilas in the world, and we need a package that conveys that.

The label that we want will be sophisticated and bold that will stand out on a shelf and be recognizable from across a bar. It needs to convey its premium status just from a glance.

Please do not use colors other than white, black, and sky/electric blue. The color scheme I see most likely winning will be some sort of white/offwhite background with black lettering, with possibly an accent of blue.

I will supply the winning logo artwork from the last contest, but if you have a better logo in mind feel free to create something new.

Please look at the link provided below for examples of the highest rated blanco tequilas.

https://www.spiritfinderhub.example/agave_spirits/blanco?q=&hPP=30&idx=BaseProduct&p=0&dFR%5Bcategory%5D%5B0%5D=Blanco

Please reference the QRL documents attached on mandatory label requirements.
Use this link for descriptions of each element of an alcohol label: https://www.qrlbureau.example/ds-labeling-home/anatomy-of-a-distilled-spirits-label-tool

Our label must have these elements:

Brand Name: Morvina
Class/Type Description: California Agave Spirit
Fanciful Name: Blanco
Alcohol Content: 40% ABV
Government Warning
Name and Address: Distilled and Bottled by Morvina Spirits, Durham, CA
Net Contents: 750 ml
Barcode
Website: www.morvinaspirits.example
Please leave a space for a brief paragraph on the back of the bottle

Thank you and good luck!

Target Market(s)

Premium Tequila Drinkers

Industry/Entity Type

Distilled Spirits

Colors

Designer to choose colors to be used in the design.

Requirements
Must have
• Please reference the QRL documents provided on required label information.

```html
<!DOCTYPE html>
<html lang="en">
<head>
<meta charset="utf-8">
<title>Morvina Blanco – Front Label</title>
<link href="https://fonts.googleapis.com/css2?family=IM+Fell+English:ital@0;1&family=IM+Fell+English+SC&display=swap" rel="stylesheet">
<style>
  :root {
    --backdrop: #eceff0;
    --label-white: #ffffff;
    --ink: #121212;
    --rule: #4a4a4a;
    --sky-blue: #3bb3e8;
    --sky-pale: #bfe3f4;
    --sketch-grey: #9a9a9a;
  }
  * { box-sizing: border-box; margin: 0; padding: 0; }
  html, body {
    width: 1200px; height: 1200px; overflow: hidden;
    background: var(--backdrop);
  }
  .canvas {
    position: relative; width: 1200px; height: 1200px;
  }
  .front-label {
    position: absolute; left: 236px; top: 52px;
    width: 728px; height: 1095px;
    background: var(--label-white);
    overflow: hidden;
    font-family: "IM Fell English SC", "IM Fell English", serif;
    color: var(--ink);
  }
  .leaf-accent {
    position: absolute; opacity: 0.55;
  }
  .leaf-accent--top {
    right: 0; top: 0; width: 270px; height: 360px;
    background: linear-gradient(225deg, var(--sky-pale) 0%, rgba(191,227,244,0.35) 45%, rgba(255,255,255,0) 80%);
  }
  .leaf-accent--bottom {
    left: 0; bottom: 0; width: 220px; height: 340px;
    background: linear-gradient(45deg, var(--sky-pale) 0%, rgba(191,227,244,0.3) 45%, rgba(255,255,255,0) 80%);
  }
  .brand {
    position: absolute; left: 0; right: 0; top: 58px;
    display: flex; flex-direction: column; align-items: center;
  }
  .brand__mark {
    width: 106px; height: 106px;
  }
  .brand__name {
    margin-top: 16px;
    font-family: "IM Fell English SC", serif;
    font-size: 40px; letter-spacing: 7px; line-height: 1;
    color: var(--ink);
  }
  .agave-art {
    position: absolute; left: 153px; top: 255px;
    width: 420px; height: 300px;
    background: radial-gradient(ellipse at 50% 70%, #c9c9c9 0%, #e4e4e4 45%, rgba(255,255,255,0) 75%);
  }
  .rule {
    position: absolute; left: 156px; width: 414px; height: 2px;
    background: var(--rule);
  }
  .rule--upper { top: 592px; }
  .rule--lower { top: 802px; }
  .class-type {
    position: absolute; left: 0; right: 0; top: 618px;
    text-align: center;
    font-size: 74px; line-height: 82px; letter-spacing: -1px;
  }
  .fanciful-name {
    position: absolute; left: 0; right: 0; top: 828px;
    text-align: center; height: 100px;
  }
  .fanciful-name__solid {
    position: relative;
    font-family: "IM Fell English SC", serif;
    font-size: 92px; line-height: 100px; letter-spacing: 1px;
    color: var(--ink);
  }
  .fanciful-name__script {
    position: absolute; left: 0; right: 0; top: 4px;
    font-family: "IM Fell English", serif; font-style: italic;
    font-size: 96px; line-height: 100px; letter-spacing: 14px;
    color: var(--sky-blue); opacity: 0.9;
  }
  .statement {
    position: absolute; left: 0; right: 0; top: 982px;
    text-align: center;
    font-family: "IM Fell English", serif;
    font-size: 21px; line-height: 34px;
  }
</style>
</head>
<body>
<main class="canvas">
  <section class="front-label">
    <div class="leaf-accent leaf-accent--top" role="img" aria-label="Faint sky-blue agave leaf sketch"></div>
    <div class="leaf-accent leaf-accent--bottom" role="img" aria-label="Faint sky-blue agave leaf sketch"></div>

    <header class="brand">
      <svg class="brand__mark" viewBox="0 0 106 106" aria-hidden="true">
        <circle cx="53" cy="53" r="50" fill="none" stroke="#121212" stroke-width="4"/>
      </svg>
      <span class="brand__name">Morvina</span>
    </header>

    <div class="agave-art" role="img" aria-label="Engraved illustration of an agave plant"></div>

    <div class="rule rule--upper"></div>
    <h1 class="class-type">California<br>Agave Spirit</h1>
    <div class="rule rule--lower"></div>

    <h2 class="fanciful-name">
      <span class="fanciful-name__solid">BLANCO</span>
      <span class="fanciful-name__script" aria-hidden="true">blanco</span>
    </h2>

    <p class="statement">40% Alc. By Vol.<br>750 ml</p>
  </section>
</main>
</body>
</html>
```